Business card and Stationery for data intelligence company

We need a new design for our business cards and stationery (Business Letter templates and a Quote example on Word, but it MUST work on Google Doc as well).

We are a software company based in Ireland and UK. Our product is "Kovar", data intelligence platform with beautiful visualizations, graph capabilities (things are interconnected), powerful, flexible, it can manage Big Data and Streaming information. It's modern and relatively open source.
Our company will provide data intelligence for law enforcements, pharmaceuticals, and similar high end customers.

We'll launch a new website soon. At the moment it's http://www.kovar-analytics.example if you want to take a look. This is our youtube channel in case you need it to understand what Kovar is: https://www.youtube.com/c/kovaranalyticschannel

We changed the logo so please use the logo I attach here.

We'd like the output to be cool and modern but elegant and "business" at the same time. It should inspire simple sophistication, "unity" "intent" "purpose" yet subtly very advanced and innovative.

The name "Kovar" does NOT refer to sirens (mithological creatures) as well as the warning devices. It means Kinetic Object Vector Analysis Reactor. Please use our logo's colors and if you want to something like the "graph" image.

```html
<!DOCTYPE html>
<html lang="en">
<head>
<meta charset="utf-8">
<title>Kovar – Business Card</title>
<link rel="stylesheet" href="https://fonts.googleapis.com/css2?family=Lato:wght@400;700&display=swap">
<style>
  :root {
    --backdrop: #0b7cb5;
    --card-dark: #333232;
    --card-light: #ffffff;
    --brand-orange: #e07b22;
    --ink: #1d1d1d;
    --faint-dark: #3e3d3d;
    --faint-light: #f3f3f3;
  }
  * { margin: 0; padding: 0; box-sizing: border-box; }
  html, body { width: 1200px; height: 1000px; overflow: hidden; }
  body {
    background: var(--backdrop);
    position: relative;
    font-family: "Lato", Arial, sans-serif;
  }
  .card {
    position: absolute;
    left: 315px;
    width: 570px;
    height: 393px;
    overflow: hidden;
  }
  .card--front {
    top: 92px;
    background: var(--card-dark);
    border-radius: 65px 0 65px 0;
  }
  .card--back {
    top: 515px;
    background: var(--card-light);
    border-radius: 0 65px 0 65px;
  }
  .faint-ring {
    position: absolute;
    border-radius: 50%;
  }
  .card--front .faint-ring {
    left: 125px; top: 35px; width: 320px; height: 320px;
    border: 20px solid var(--faint-dark);
  }
  .card--back .faint-ring {
    left: 120px; top: 30px; width: 330px; height: 330px;
    border: 24px solid var(--faint-light);
  }
  .brand { position: absolute; }
  .brand__dot {
    position: absolute;
    border-radius: 50%;
    background: var(--brand-orange);
  }
  .brand__name {
    position: absolute;
    font-family: "Lato", Arial, sans-serif;
    font-weight: 700;
    color: var(--brand-orange);
    white-space: nowrap;
    line-height: 1;
  }
  .card--front .brand__dot { left: 128px; top: 153px; width: 90px; height: 90px; }
  .card--front .brand__name { left: 238px; top: 174px; font-size: 48px; }
  .card--back .brand__dot { left: 325px; top: 29px; width: 58px; height: 58px; }
  .card--back .brand__name { left: 395px; top: 43px; font-size: 30px; }

  .holder {
    position: absolute;
    left: 32px; top: 160px;
    padding-left: 8px;
    border-left: 2px solid var(--brand-orange);
    font-size: 16px;
    font-weight: 700;
    line-height: 20px;
  }
  .holder__name { color: var(--brand-orange); }
  .holder__role { color: var(--ink); }

  .address {
    position: absolute;
    right: 41px; top: 139px;
    text-align: right;
    font-size: 16px;
    line-height: 20.5px;
    color: var(--ink);
    font-style: normal;
  }
  .contacts {
    position: absolute;
    right: 41px; top: 303px;
    list-style: none;
  }
  .contacts__item {
    display: flex;
    justify-content: flex-end;
    align-items: center;
    gap: 5px;
    height: 20px;
    font-size: 16px;
    color: var(--ink);
  }
  .contacts__icon {
    width: 16px; height: 16px;
    display: block;
  }
</style>
</head>
<body>

  <section class="card card--front" aria-label="Card front">
    <div class="faint-ring"></div>
    <div class="brand">
      <span class="brand__dot"></span>
      <span class="brand__name">Kovar</span>
    </div>
  </section>

  <section class="card card--back" aria-label="Card back">
    <div class="faint-ring"></div>
    <div class="brand">
      <span class="brand__dot"></span>
      <span class="brand__name">Kovar</span>
    </div>

    <div class="holder">
      <div class="holder__name">Daniel Byrne</div>
      <div class="holder__role">CEO</div>
    </div>

    <address class="address">
      Unit 7<br>
      Corrib Innovation Park<br>
      Eastfield, Lisheen - Ireland
    </address>

    <ul class="contacts">
      <li class="contacts__item">+353 87 5550142
        <svg class="contacts__icon" viewBox="0 0 16 16" aria-hidden="true">
          <rect width="16" height="16" fill="#e07b22"/>
          <path d="M5 3.5 L6.6 3.5 L7.3 5.8 L6.3 6.6 Q7.2 8.6 9.2 9.6 L10 8.6 L12.5 9.3 L12.5 11 Q12 12.5 10.5 12.3 Q4.5 11.2 3.7 5 Q3.8 3.6 5 3.5 Z" fill="#fff"/>
        </svg>
      </li>
      <li class="contacts__item">www.kovar-analytics.example
        <svg class="contacts__icon" viewBox="0 0 16 16" aria-hidden="true">
          <rect width="16" height="16" fill="#e07b22"/>
          <rect x="3.5" y="4" width="9" height="6" fill="none" stroke="#fff" stroke-width="1.3"/>
          <rect x="7.3" y="10" width="1.4" height="1.6" fill="#fff"/>
          <rect x="5.5" y="11.6" width="5" height="1.2" fill="#fff"/>
        </svg>
      </li>
      <li class="contacts__item">info@kovar-analytics.example
        <svg class="contacts__icon" viewBox="0 0 16 16" aria-hidden="true">
          <rect width="16" height="16" fill="#e07b22"/>
          <rect x="3.5" y="5" width="9" height="6.5" fill="#fff"/>
          <path d="M3.5 5 L8 8.6 L12.5 5" fill="none" stroke="#e07b22" stroke-width="1"/>
        </svg>
      </li>
    </ul>
  </section>

</body>
</html>
```